Corbrook Estates LLC stationary for a real estate property management company.

Create stationary (letterhead, envelopes, business cards) using Corbrook Estates LLC logo as primary creative element. Stationary design needs to be horizontal, leaving as much space as possible for correspondence copy. See attached Creative Brief and past stationary files for details.

Target Market(s)

Prospective apartment residents and current residents, vendors, and government agencies.

Industry/Entity Type

Property Management

Contact Information for Business Card

Business card employee title: Property Manager. Should include address, phone, fax, email, website, slogan, and Corbrook Estates logo.

Font styles to use
Sans Serif

Colors
0592cd
000000

Requirements
Must have
• Tone should be conservative, institutional, business (i.e. banking, finance, real estate). Must include: address, phone, fax, website, and slogan (see attached Creative Brief). Should be a horizontal design, leaving as much room as possible for letter correspondence copy.
Nice to have
• Please use an Arial or Helvetica style font.
Should not have
• Letterhead layout should leave as much room as possible for copy.

```html
<!DOCTYPE html>
<html lang="en">
<head>
<meta charset="utf-8">
<title>Corbrook Estates LLC – Stationery</title>
<link href="https://fonts.googleapis.com/css2?family=Arimo:wght@400;700&display=swap" rel="stylesheet">
<style>
  :root {
    --backdrop: #e8e8e8;
    --paper: #ffffff;
    --brand-blue: #0e6ea9;
    --ink: #111111;
    --ink-soft: #555555;
    --muted: #888888;
    --crop: #777777;
  }
  * { margin: 0; padding: 0; box-sizing: border-box; }
  html, body {
    width: 1200px; height: 1200px; overflow: hidden;
    background: var(--backdrop);
    font-family: "Arimo", Arial, Helvetica, sans-serif;
  }
  .canvas { position: relative; width: 1200px; height: 1200px; }
  .sheet { position: absolute; background: var(--paper); overflow: hidden; }
  .crop-marks { position: absolute; inset: 0; width: 100%; height: 100%; pointer-events: none; }
  .crop-marks line { stroke: var(--crop); stroke-width: 0.8; }

  .brand-name {
    color: var(--brand-blue);
    font-weight: 700;
    letter-spacing: -0.3px;
    white-space: nowrap;
    display: flex; align-items: center;
  }
  .brand-name .brand-dot {
    display: inline-block; background: var(--brand-blue); border-radius: 50%;
    flex: none;
  }

  /* Envelope */
  .envelope { left: 165px; top: 50px; width: 870px; height: 410px; }
  .envelope .brand-block { position: absolute; left: 63px; top: 88px; }
  .envelope .brand-name { font-size: 36px; }
  .envelope .brand-dot { width: 28px; height: 28px; margin-right: 12px; }
  .envelope .return-address { margin-top: 14px; margin-left: 40px; font-size: 14px; color: var(--ink); letter-spacing: -0.2px; }
  .envelope .base-band { position: absolute; left: 0; right: 0; top: 360px; height: 46px; background: var(--brand-blue); }

  /* Letterhead */
  .letterhead { left: 96px; top: 493px; width: 501px; height: 637px; }
  .letterhead .brand-block { position: absolute; left: 30px; top: 36px; }
  .letterhead .brand-name { font-size: 17px; }
  .letterhead .brand-dot { width: 14px; height: 14px; margin-right: 6px; }
  .letterhead .slogan { font-size: 8.5px; color: var(--muted); margin-top: 4px; }
  .letterhead .footer-band {
    position: absolute; left: 10px; top: 597px; width: 481px; height: 33px;
    background: var(--brand-blue); color: #fff; font-size: 8px;
    display: flex; align-items: center; justify-content: center;
  }

  /* Business card */
  .business-card { left: 670px; top: 676px; width: 473px; height: 270px; }
  .business-card .brand-block { position: absolute; left: 17px; top: 36px; }
  .business-card .brand-name { font-size: 23px; }
  .business-card .brand-dot { width: 18px; height: 18px; margin-right: 8px; }
  .business-card .slogan { font-size: 13px; color: var(--muted); margin-top: 6px; }
  .business-card .person-name {
    position: absolute; left: 0; width: 472px; top: 124px; text-align: center;
    font-size: 22px; font-weight: 700; color: var(--brand-blue);
  }
  .business-card .person-title {
    position: absolute; left: 0; width: 472px; top: 152px; text-align: center;
    font-size: 12px; color: var(--ink-soft);
  }
  .business-card .address { position: absolute; left: 17px; top: 218px; font-size: 13px; line-height: 16px; color: var(--ink-soft); }
  .business-card .contact-list {
    position: absolute; right: 17px; top: 186px; text-align: right;
    font-size: 12px; line-height: 16px; color: var(--ink-soft); list-style: none;
  }
  .business-card .base-rule { position: absolute; left: 0; right: 0; top: 264px; height: 6px; background: var(--brand-blue); }
</style>
</head>
<body>
<main class="canvas">

  <section class="sheet envelope" aria-label="Envelope">
    <div class="brand-block">
      <div class="brand-name"><span class="brand-dot"></span>Corbrook Estates LLC</div>
      <p class="return-address">2870 Alder Ridge Road #B212, Riverton, CA 92408</p>
    </div>
    <div class="base-band"></div>
    <svg class="crop-marks" viewBox="0 0 870 410">
      <line x1="27" y1="0" x2="27" y2="20"/><line x1="0" y1="27" x2="20" y2="27"/>
      <line x1="843" y1="0" x2="843" y2="20"/><line x1="850" y1="27" x2="870" y2="27"/>
      <line x1="27" y1="390" x2="27" y2="410"/><line x1="0" y1="383" x2="20" y2="383"/>
      <line x1="843" y1="390" x2="843" y2="410"/><line x1="850" y1="383" x2="870" y2="383"/>
    </svg>
  </section>

  <section class="sheet letterhead" aria-label="Letterhead">
    <div class="brand-block">
      <div class="brand-name"><span class="brand-dot"></span>Corbrook Estates LLC</div>
      <p class="slogan">Multifamily Property Management</p>
    </div>
    <div class="footer-band">2870 Alder Ridge Road #B212, Riverton, CA 92408 | www.corbrookestates.us</div>
    <svg class="crop-marks" viewBox="0 0 501 637">
      <line x1="16" y1="0" x2="16" y2="12"/><line x1="0" y1="16" x2="12" y2="16"/>
      <line x1="485" y1="0" x2="485" y2="12"/><line x1="489" y1="16" x2="501" y2="16"/>
      <line x1="16" y1="625" x2="16" y2="637"/><line x1="0" y1="621" x2="12" y2="621"/>
      <line x1="485" y1="625" x2="485" y2="637"/><line x1="489" y1="621" x2="501" y2="621"/>
    </svg>
  </section>

  <section class="sheet business-card" aria-label="Business card">
    <div class="brand-block">
      <div class="brand-name"><span class="brand-dot"></span>Corbrook Estates LLC</div>
      <p class="slogan">Multifamily Property Management</p>
    </div>
    <p class="person-name">&lt;Name&gt;</p>
    <p class="person-title">Property Manager</p>
    <p class="address">2870 Alder Ridge Road #B212<br>Riverton, CA 92408</p>
    <ul class="contact-list">
      <li>Phone: (555) 014-2870</li>
      <li>Fax: (555) 014-2871</li>
      <li>info@corbrookestates.us</li>
      <li>www.corbrookestates.us</li>
    </ul>
    <div class="base-rule"></div>
  </section>

</main>
</body>
</html>
```